Poster Design For Obstacle Run

Design a poster for the Copper Dune Obstacle run.
Text: Copper Dune Obstacle Run. May 12th, 2018. Sittard. www.copperdunerun.nl. I have added a lot of pictures.
Furthermore, the logo should be included. As an example I included a poster from the valkor race that we really like (valkor team challenge) and also. Feel free to take a look at our website for inspiration: www.copperdunerun.nl

```html
<!DOCTYPE html>
<html lang="en">
<head>
<meta charset="utf-8">
<title>Copper Dune Obstacle Run – Poster</title>
<link href="https://fonts.googleapis.com/css2?family=Rubik+Dirt&family=Arimo:wght@400;700&display=swap" rel="stylesheet">
<style>
  :root {
    --page-bg: #e8e8eb;
    --rust: #c9521f;
    --rust-deep: #a9401a;
    --mud-dark: #6a300f;
    --mud-mid: #c0581c;
    --mud-light: #e58a35;
    --water: #c9a27a;
    --shirt-red: #e5322a;
    --field-green: #6f8f4a;
    --ink: #141414;
    --paper: #f6ece4;
  }
  * { margin: 0; padding: 0; box-sizing: border-box; }
  html, body {
    width: 1018px;
    height: 1200px;
    overflow: hidden;
    background: var(--page-bg);
  }
  .poster {
    position: absolute;
    left: 80px;
    top: 0;
    width: 858px;
    height: 1200px;
    overflow: hidden;
    background: var(--rust);
  }
  .hero-photo {
    position: absolute;
    left: 0;
    top: 0;
    width: 858px;
    height: 960px;
    background:
      radial-gradient(ellipse 260px 200px at 62% 68%, rgba(229,50,42,0.95) 0%, rgba(229,50,42,0.6) 50%, rgba(229,50,42,0) 100%),
      radial-gradient(ellipse 120px 150px at 74% 36%, rgba(90,40,25,0.75) 0%, rgba(90,40,25,0) 100%),
      radial-gradient(ellipse 420px 110px at 40% 47%, rgba(201,162,122,0.85) 0%, rgba(201,162,122,0) 100%),
      linear-gradient(180deg, rgba(111,143,74,0.9) 0%, rgba(111,143,74,0.35) 9%, rgba(111,143,74,0) 16%),
      linear-gradient(100deg, var(--mud-light) 0%, var(--mud-mid) 45%, var(--mud-dark) 100%);
  }
  .torn-band {
    position: absolute;
    left: 0;
    top: 900px;
    width: 858px;
    height: 300px;
  }
  .event-badge {
    position: absolute;
    left: 419px;
    top: 860px;
    transform: translate(-50%, -50%);
    display: flex;
    flex-direction: column;
    align-items: center;
    gap: 6px;
    padding: 22px 30px;
    background: var(--ink);
    border-radius: 50%;
    width: 300px;
    height: 200px;
    justify-content: center;
  }
  .event-badge__place {
    font-family: "Arimo", Arial, sans-serif;
    font-weight: 700;
    font-size: 13px;
    letter-spacing: 4px;
    color: var(--paper);
  }
  .event-badge__name {
    font-family: "Arimo", Arial, sans-serif;
    font-weight: 700;
    font-size: 20px;
    line-height: 1.15;
    color: var(--paper);
    text-transform: uppercase;
    text-align: center;
    width: 190px;
  }
  .event-badge__dot {
    width: 12px;
    height: 12px;
    border-radius: 50%;
    background: var(--rust);
  }
  .headline {
    position: absolute;
    left: 0;
    width: 858px;
    top: 978px;
    text-align: center;
    font-family: "Rubik Dirt", "Arimo", sans-serif;
    font-weight: 400;
    font-size: 86px;
    line-height: 1;
    letter-spacing: 1px;
    color: var(--paper);
  }
  .details {
    position: absolute;
    left: 0;
    width: 858px;
    top: 1086px;
    text-align: center;
    font-family: "Arimo", Arial, sans-serif;
    font-weight: 700;
    font-size: 34px;
    line-height: 1.2;
    color: var(--paper);
    white-space: nowrap;
  }
  .details__divider {
    display: inline-block;
    margin: 0 26px;
  }
</style>
</head>
<body>
  <main class="poster">
    <div class="hero-photo" role="img" aria-label="Runner in a red shirt splashing through an orange mud pit, grass at the top edge"></div>

    <svg class="torn-band" viewBox="0 0 858 300" aria-hidden="true">
      <path fill="var(--rust)" d="M0 42 L30 36 L58 46 L90 32 L120 42 L150 28 L190 40 L230 34 L262 46 L300 38 L340 46 L380 36 L430 44 L470 30 L520 42 L560 34 L600 46 L640 36 L690 42 L730 28 L770 40 L810 34 L858 42 L858 300 L0 300 Z"/>
      <path fill="var(--ink)" d="M0 280 L40 274 L80 282 L140 272 L200 280 L260 270 L320 282 L380 274 L440 280 L500 270 L560 282 L620 274 L680 280 L740 270 L800 280 L858 274 L858 300 L0 300 Z"/>
    </svg>

    <div class="event-badge">
      <span class="event-badge__place">SITTARD</span>
      <span class="event-badge__name">Copper Dune Obstacle Run</span>
      <span class="event-badge__dot"></span>
    </div>

    <h1 class="headline">OBSTACLE RUN</h1>
    <p class="details">MAY 12TH, 2018<span class="details__divider">|</span>www.copperdunerun.nl</p>
  </main>
</body>
</html>
```